Brightpath Growth Forum

I need a first class flyer that screams success and makes people want to come to our event.
I will provide a flyer that was just done that I wasn't satisfied with. Please take the info from the flyer and give me something amazing that I can be proud of and say WOW!!
I will include a few pictures to choose from. You can use some or all.
Thanks in advance
Updates
Hey designers,
Here is a link to more pictures for flyer design. Please ignore the flyers already in file from a past event.
https://files.quelvanshare.com/s/r82kd7vn3p5xmqzet1wa
Industry/Entity Type
Leadership
Colors
Designer to choose colors to be used in the design.
Look and feel
Each slider illustrates characteristics of the customer's brand and the style your logo design should communicate.

```html
<!DOCTYPE html>
<html lang="en">
<head>
<meta charset="utf-8">
<title>Brightpath Growth Forum</title>
<link href="https://fonts.googleapis.com/css2?family=Roboto+Condensed:wght@400;700&family=Open+Sans:wght@300;400&display=swap" rel="stylesheet">
<style>
  :root {
    --backdrop: #2b2b2b;
    --gold: #d8ab58;
    --gold-light: #f0d08f;
    --gold-pale: #fbe7b5;
    --slate: #6c7071;
    --slate-dark: #55595a;
    --slate-deep: #4a4e4f;
    --white: #ffffff;
    --photo-a: #8a8f96;
    --photo-b: #b8413f;
  }
  * { margin: 0; padding: 0; box-sizing: border-box; }
  html, body { width: 1022px; height: 1200px; overflow: hidden; background: var(--backdrop); }
  .flyer {
    position: absolute; left: 152px; top: 70px; width: 716px; height: 1015px;
    overflow: hidden; color: var(--white);
    font-family: "Roboto Condensed", "Arial Narrow", sans-serif;
  }
  .flyer-shapes { position: absolute; inset: 0; }
  .txt { position: absolute; line-height: 1; white-space: nowrap; }
  .center { left: 0; width: 100%; text-align: center; }
  .org-line { left: 0; width: 376px; text-align: center; top: 42px; font-size: 20px; }
  .title {
    left: 40px; width: 300px; font-weight: 700; font-size: 48px; letter-spacing: .5px;
    color: var(--gold-pale); text-shadow: 0 2px 2px rgba(120,80,20,.35);
  }
  .title-1 { top: 70px; }
  .title-2 { top: 117px; }
  .title-sub { left: 45px; top: 172px; font-family: "Open Sans", sans-serif; font-size: 34px; font-weight: 400; }
  .date { left: 40px; width: 200px; text-align: center; }
  .date-month { top: 307px; font-family: "Open Sans", sans-serif; font-weight: 300; font-size: 40px; }
  .date-days { top: 350px; font-weight: 700; font-size: 31px; color: var(--gold-light); }
  .date-year { top: 382px; font-family: "Open Sans", sans-serif; font-weight: 300; font-size: 28px; }
  .pitch { top: 436px; font-weight: 700; font-size: 19px; }
  .hosts { top: 469px; font-weight: 700; font-size: 38px; color: var(--gold-pale); letter-spacing: 1px; text-shadow: 0 2px 2px rgba(0,0,0,.25); }
  .intro { left: 39px; top: 542px; font-weight: 700; font-size: 19px; }
  .benefits { position: absolute; list-style: none; font-size: 17.5px; line-height: 24.5px; }
  .benefits li { position: relative; padding-left: 24px; }
  .benefits li::before {
    content: ""; position: absolute; left: 3px; top: 9px; width: 8px; height: 8px;
    border-radius: 50%; background: var(--gold);
  }
  .benefits-left { left: 54px; top: 576px; }
  .benefits-right { left: 391px; top: 576px; }
  .cta-line { top: 687px; font-size: 17.5px; }
  .cta-line strong { color: var(--gold-light); }
  .quote { top: 742px; font-weight: 700; font-size: 19.5px; }
  .quote-highlight { top: 775px; font-family: "Open Sans", sans-serif; font-size: 27px; color: var(--gold-light); }
  .details { position: absolute; font-size: 16px; line-height: 20.5px; }
  .schedule { left: 39px; top: 858px; }
  .venue { left: 433px; top: 858px; }
  .host-mark {
    position: absolute; left: 301px; top: 850px; width: 120px; text-align: center;
    font-weight: 700; font-size: 14px; line-height: 15px; text-transform: uppercase;
  }
  .host-mark .dot { display: block; width: 14px; height: 14px; border-radius: 50%; background: var(--white); margin: 0 auto 5px; }
  .register-label { top: 951px; font-weight: 700; font-size: 14px; }
  .register-url { top: 968px; font-size: 18px; }
</style>
</head>
<body>
<article class="flyer">
  <svg class="flyer-shapes" width="716" height="1015" viewBox="0 0 716 1015">
    <defs>
      <linearGradient id="goldPanel" x1="0" y1="0" x2="1" y2="1">
        <stop offset="0" stop-color="#cfa053"/>
        <stop offset=".5" stop-color="#e0b66b"/>
        <stop offset="1" stop-color="#c7994d"/>
      </linearGradient>
      <linearGradient id="slateBody" x1="0" y1="0" x2="0" y2="1">
        <stop offset="0" stop-color="#5f6364"/>
        <stop offset=".25" stop-color="#7d8182"/>
        <stop offset=".5" stop-color="#5a5e5f"/>
        <stop offset="1" stop-color="#4e5253"/>
      </linearGradient>
      <linearGradient id="photoTone" x1="0" y1="0" x2="1" y2="1">
        <stop offset="0" stop-color="#c7ccd2"/>
        <stop offset=".45" stop-color="#5a6070"/>
        <stop offset="1" stop-color="#b8413f"/>
      </linearGradient>
      <linearGradient id="bandTone" x1="0" y1="0" x2="0" y2="1">
        <stop offset="0" stop-color="#4c5051"/>
        <stop offset=".2" stop-color="#6a6e6f"/>
        <stop offset="1" stop-color="#5d6162"/>
      </linearGradient>
    </defs>
    <rect width="716" height="1015" fill="url(#slateBody)"/>
    <rect y="528" width="716" height="192" fill="url(#bandTone)"/>
    <rect y="720" width="716" height="295" fill="#575b5c"/>
    <polygon points="0,0 463,0 340,320 0,230" fill="url(#goldPanel)"/>
    <polygon points="0,230 340,320 346,326 0,240" fill="#e9c47a"/>
    <polygon points="463,0 716,0 716,420 340,320" fill="url(#photoTone)" role="img" aria-label="Photo of the two event hosts standing together outside a modern building"/>
    <polygon points="463,0 470,0 348,322 340,320" fill="#f0d08f"/>
    <polygon points="340,320 716,420 716,430 340,328" fill="#e0b66b"/>
    <polygon points="0,952 250,1015 0,1015" fill="url(#goldPanel)"/>
  </svg>

  <p class="txt org-line">The Hollis Leadership Development</p>
  <h1 class="txt title title-1">BRIGHTPATH</h1>
  <p class="txt title title-2">GROWTH</p>
  <p class="txt title-sub">Forum</p>

  <p class="txt date date-month">JULY</p>
  <p class="txt date date-days">25th &amp; 26th</p>
  <p class="txt date date-year">2014</p>

  <p class="txt center pitch">Want to be personally coached and trained by multi-million dollar earners?</p>
  <h2 class="txt center hosts">MARCUS &amp; DANA HOLLIS</h2>

  <p class="txt intro">At this 2-days power-packed events, you will learn how to:</p>
  <ul class="benefits benefits-left">
    <li>Maximize your income</li>
    <li>Gain leadership mastery skills</li>
    <li>Grow your team &amp; your customer base</li>
  </ul>
  <ul class="benefits benefits-right">
    <li>Effectively manage your time</li>
    <li>Present like a pro</li>
    <li>Build a massive top-producing<br>business &amp; much more</li>
  </ul>
  <p class="txt center cta-line">If you are ready to <strong>Become a top Money Earner</strong> This is an event you do not want to miss!</p>

  <p class="txt center quote">"We will teach you step-by-step how to build a dynasty and become a</p>
  <p class="txt center quote-highlight">Million-Dollar Earner…”</p>

  <p class="details schedule"><strong>Friday:</strong> 9:00am to 5:00pm (CST)<br><strong>Saturday:</strong> 9:00am to 5:00pm (CST)<br>Seating limited to the 1st 100 to register!</p>
  <div class="host-mark"><span class="dot"></span>The Summit<br>Circle</div>
  <p class="details venue">The Summit Circle Training Center<br>4120 Meridian Parkway, Suite #800,<br>Fairbrook, Texas 75099</p>

  <p class="txt center register-label">Register online at:</p>
  <p class="txt center register-url">www.summitcircleleadershipevent.com</p>
</article>
</body>
</html>
```